Brindle Works - Fast, Efficient and Gas Mainteance for Domestic, Commercial and Industrial clients

We are in the process of purchasing a new business and would like to get a new logo and business card.
Business is a gas maintenance business that also does new gas installations.
Has been established since 1988.
Services include:
Install all types of gas appliances & equipment inc. hot water units
Maintain / repair / replace all types of gas appliances & equipment

Target Market(s)

Domestic, Commercial and Industrial clients

Industry/Entity Type

Business

Contact Information for Business Card

admin@brindleworks-example.com.au
07 5981 4726
Brindle Works PTY LTD

Logo Text

Gas Fitting & Plumbing Maintenance Specialists

Font styles to use
Sans Serif

Requirements
Must have
• Logo
• Business name, contact number, email address, web address
• Domestic | Commercial | Industrial Est Since 1988
Nice to have
• Possibly a black card with a flame logo to one side
Should not have
• Spelling errors

```html
<!DOCTYPE html>
<html lang="en">
<head>
<meta charset="utf-8">
<title>Brindle Works – Business Card</title>
<link rel="stylesheet" href="https://fonts.googleapis.com/css2?family=Noto+Serif:wght@400;700&family=Open+Sans:wght@400;700&family=Great+Vibes&display=swap">
<style>
  :root{
    --backdrop:#e9e6e1;
    --paper:#f4f4f4;
    --ink-black:#0c0c0c;
    --band-grey:#3a3a3a;
    --accent:#e8674a;
    --accent-light:#f08a6c;
    --text-grey:#4a4d52;
    --text-soft:#8a8d92;
    --white:#ffffff;
  }
  *{margin:0;padding:0;box-sizing:border-box}
  html,body{width:1200px;height:892px;overflow:hidden;background:var(--backdrop)}
  .canvas{position:relative;width:1200px;height:892px}
  .card{position:absolute;top:281px;width:540px;height:330px;border-radius:4px;overflow:hidden;box-shadow:0 6px 18px rgba(0,0,0,.18)}
  .card--front{left:40px;background:var(--ink-black)}
  .card--back{left:620px;background:linear-gradient(160deg,#1c1c1c,#050505 60%,#141414)}
  .card__shapes{position:absolute;inset:0}

  .brand{position:absolute;left:24px;top:100px}
  .brand__name{position:relative;display:inline-flex;align-items:center;gap:8px;font-family:"Noto Serif",serif;font-weight:700;font-size:27px;line-height:34px;color:var(--accent);letter-spacing:.3px;text-transform:uppercase;white-space:nowrap}
  .brand__mark{width:9px;height:9px;border-radius:50%;background:var(--accent)}
  .brand__suffix{position:absolute;right:0;top:-6px;font-family:"Open Sans",sans-serif;font-weight:700;font-size:7px;line-height:8px;color:var(--text-grey);letter-spacing:.3px}
  .brand__tagline{font-family:"Open Sans",sans-serif;font-weight:700;font-size:14px;color:var(--text-grey);margin-top:2px;white-space:nowrap}
  .brand__sectors{font-family:"Open Sans",sans-serif;font-size:8.5px;color:var(--text-soft);margin-top:4px;display:flex;align-items:baseline;gap:8px;white-space:nowrap}
  .brand__since{font-family:"Great Vibes",cursive;font-size:16px;color:var(--text-soft)}

  .appliance{position:absolute;right:16px;top:22px;width:100px;height:90px;border-radius:3px;
    background:linear-gradient(135deg,#c9ccd0 0%,#8f9398 45%,#d9582c 70%,#6b6e72 100%)}

  .contact{position:absolute;left:374px;top:218px;list-style:none;font-family:"Open Sans",sans-serif;font-size:9px;line-height:14px;color:var(--white);white-space:nowrap}
  .contact__icons{position:absolute;left:364px;top:300px;display:flex;gap:5px}
  .contact__icon{width:9px;height:9px;background:rgba(255,255,255,.75);border-radius:1px}

  .back__text{position:absolute;left:40px;top:118px}
  .back__name{font-family:"Noto Serif",serif;font-size:28px;color:var(--accent)}
  .back__line{font-family:"Open Sans",sans-serif;font-size:14px;color:var(--white);margin-top:6px}
</style>
</head>
<body>
<main class="canvas">

  <section class="card card--front" aria-label="Business card front">
    <svg class="card__shapes" viewBox="0 0 540 330" aria-hidden="true">
      <defs>
        <linearGradient id="accentFill" x1="0" y1="1" x2="1" y2="0">
          <stop offset="0" stop-color="#e8674a"/>
          <stop offset=".5" stop-color="#f08a6c"/>
          <stop offset="1" stop-color="#e8674a"/>
        </linearGradient>
      </defs>
      <path d="M0 0 H370 C325 110 300 220 290 330 H0Z" fill="#f4f4f4"/>
      <path d="M410 0 H428 C388 110 363 220 353 330 H335 C345 220 370 110 410 0Z" fill="#3a3a3a"/>
      <path d="M428 0 H540 V330 H353 C363 220 388 110 428 0Z" fill="url(#accentFill)"/>
    </svg>

    <div class="brand">
      <div class="brand__name"><span class="brand__mark"></span>Brindle Works<span class="brand__suffix">PTY LTD</span></div>
      <p class="brand__tagline">Gas fitting &amp; Plumbing Specialists</p>
      <p class="brand__sectors">Domestic | Commercial | Industrial <span class="brand__since">Est Since 1988</span></p>
    </div>

    <div class="appliance" role="img" aria-label="Photo of gas heater with flame and hot water units"></div>

    <ul class="contact">
      <li>07 5981 4726</li>
      <li>07 5981 4739</li>
      <li>www.brindleworks-example.com.au</li>
      <li>admin@brindleworks-example.com.au</li>
      <li>PO Box 2846, Palm Ridge, QLD 4230</li>
    </ul>
    <div class="contact__icons" aria-hidden="true">
      <span class="contact__icon"></span><span class="contact__icon"></span><span class="contact__icon"></span><span class="contact__icon"></span><span class="contact__icon"></span>
    </div>
  </section>

  <section class="card card--back" aria-label="Business card back">
    <div class="back__text">
      <h1 class="back__name">Brindle Works PTY LTD</h1>
      <p class="back__line">Gas fitting &amp; Plumbing Specialists</p>
      <p class="back__line">Domestic | Commercial | Industrial Est Since 1988</p>
    </div>
  </section>

</main>
</body>
</html>
```